Modern business card design for professional copywriter

I'd like a business card design that I can use to have my cards printed out by tavrel.com as a squared corners business card (see artwork and design guidelines here: https://help.tavrel.com/hc/en-gb/sections/300481762-TAVREL-Product-Templates)

The design should be clean and modern and reflect the colours, tone and branding on my website: https://gretafolvane.com.au

Target Market(s)

Professionals, B2B small business owners

Industry/Entity Type

Business

Contact Information for Business Card

Greta Folvane
m: 0427 954 368
e: greta@gretafolvane.com.au
w: gretafolvane.com.au

Font styles to use
Sans Serif

Requirements
Must have
• Tagline: "Smart copywriting for clever business people"
• Brand colours: fd8000, 009984, 666666 and black
Nice to have

```html
<!DOCTYPE html>
<html lang="en">
<head>
<meta charset="utf-8">
<title>Greta Folvane – Business Card</title>
<link rel="stylesheet" href="https://fonts.googleapis.com/css2?family=Jost:wght@400;500&display=swap">
<style>
  :root {
    --teal: #179b85;
    --orange: #fd8000;
    --grey: #666666;
    --ink: #2a2a2a;
    --paper: #ffffff;
    --backdrop: #eeece8;
  }
  * { margin: 0; padding: 0; box-sizing: border-box; }
  html, body {
    width: 1200px; height: 929px; overflow: hidden;
    background: var(--backdrop);
    font-family: "Jost", "Futura", sans-serif;
  }
  .stage { position: relative; width: 1200px; height: 929px; }
  .card {
    position: absolute;
    width: 520px; height: 336px;
    box-shadow: 0 4px 14px rgba(0,0,0,0.18);
  }
  .card--front {
    left: 70px; top: 110px;
    background: var(--teal);
    display: flex; align-items: center; justify-content: center;
  }
  .wordmark {
    font-weight: 500;
    font-size: 40px;
    letter-spacing: 0.5px;
    display: flex; align-items: center; gap: 12px;
  }
  .wordmark__dot {
    width: 14px; height: 14px; border-radius: 50%;
  }
  .card--front .wordmark { color: var(--paper); }
  .card--front .wordmark__dot { background: var(--paper); }

  .card--back {
    left: 610px; top: 480px;
    background: var(--paper);
  }
  .card--back .wordmark {
    position: absolute; right: 34px; top: 46px;
    font-size: 28px; color: var(--teal);
  }
  .card--back .wordmark__dot { background: var(--orange); width: 11px; height: 11px; }
  .name-band {
    position: absolute; left: 0; top: 118px;
    width: 300px; height: 62px;
    background: var(--teal);
    color: var(--paper);
    padding: 8px 0 0 34px;
    line-height: 1.1;
  }
  .name-band__name { font-size: 22px; font-weight: 500; }
  .name-band__role { font-size: 17px; }
  .tagline {
    position: absolute; right: 34px; top: 190px;
    text-align: right;
    font-size: 13px; line-height: 1.25;
    color: var(--ink);
  }
  .contacts {
    position: absolute; left: 34px; bottom: 34px;
    list-style: none;
    font-size: 15px; line-height: 1.45;
    color: var(--ink);
  }
  .contacts li { display: flex; align-items: center; gap: 10px; }
  .contacts svg { width: 12px; height: 12px; flex: none; }
</style>
</head>
<body>
<main class="stage">
  <section class="card card--front" aria-label="Card front">
    <div class="wordmark"><span class="wordmark__dot"></span>Greta Folvane</div>
  </section>

  <section class="card card--back" aria-label="Card back">
    <div class="wordmark"><span class="wordmark__dot"></span>Greta Folvane</div>
    <div class="name-band">
      <div class="name-band__name">Greta Folvane</div>
      <div class="name-band__role">Copywriter</div>
    </div>
    <p class="tagline">Smart copywriting for<br>clever business people</p>
    <ul class="contacts">
      <li>
        <svg viewBox="0 0 12 12"><rect x="3" y="0.8" width="6" height="10.4" rx="1" fill="none" stroke="#fd8000" stroke-width="1.3"/></svg>
        0427 954 368
      </li>
      <li>
        <svg viewBox="0 0 12 12"><rect x="0.5" y="2" width="11" height="8" fill="#fd8000"/><path d="M0.5 2 L6 6.5 L11.5 2" fill="none" stroke="#fff" stroke-width="1"/></svg>
        greta@gretafolvane.com.au
      </li>
      <li>
        <svg viewBox="0 0 12 12"><circle cx="5" cy="5" r="3.5" fill="none" stroke="#fd8000" stroke-width="1.6"/><path d="M7.5 7.5 L11 11" stroke="#fd8000" stroke-width="1.8"/></svg>
        gretafolvane.com.au
      </li>
    </ul>
  </section>
</main>
</body>
</html>
```